Build a Website for Bramble and Pike

We have a client who would like their website redesigned including the graphics and a shopping cart all using Wordpress- see attached document and existing site is brambleandpike.example

We would like front page done along with a banner to allow us to pick a winner

```html
<!DOCTYPE html>
<html lang="en">
<head>
<meta charset="utf-8">
<title>Bramble and Pike — The Equipment Security Specialists</title>
<link href="https://fonts.googleapis.com/css2?family=Open+Sans:wght@300;400;600;700&family=Roboto+Condensed:wght@700&family=Raleway:wght@300&display=swap" rel="stylesheet">
<style>
  :root {
    --brand-navy: #1d3f6e;
    --brand-blue: #1a86c8;
    --button-blue: #1482c6;
    --ink: #111111;
    --text-grey: #6f6f6f;
    --light-grey: #8a8a8a;
    --rule-grey: #d9d9d9;
    --hero-light: #d9d2c6;
    --hero-mid: #a39a86;
    --hero-dark: #565645;
    --panel-white: rgba(240, 236, 230, 0.82);
    --connector: #e8e8e8;
    --white: #ffffff;
  }
  * { margin: 0; padding: 0; box-sizing: border-box; }
  html, body { width: 1200px; height: 1079px; overflow: hidden; background: var(--white); }
  body { position: relative; font-family: "Open Sans", Arial, sans-serif; color: var(--ink); }

  .site-header { position: absolute; left: 0; top: 0; width: 1200px; height: 124px; background: var(--white); }
  .brand { position: absolute; left: 113px; top: 38px; display: flex; align-items: center; gap: 12px; }
  .brand-mark { width: 30px; height: 30px; background: var(--brand-navy); }
  .brand-text { display: flex; flex-direction: column; }
  .brand-name { font-family: "Roboto Condensed", Arial, sans-serif; font-weight: 700; font-size: 36px; line-height: 38px; color: var(--brand-navy); text-transform: uppercase; letter-spacing: 0.5px; }
  .brand-tagline { font-family: "Roboto Condensed", Arial, sans-serif; font-weight: 700; font-size: 15.5px; line-height: 18px; color: var(--brand-navy); text-transform: uppercase; }
  .main-nav { position: absolute; top: 53px; left: 532px; display: flex; font-size: 17px; color: var(--ink); }
  .main-nav a { color: inherit; text-decoration: none; margin-right: 25px; white-space: nowrap; }
  .main-nav a:last-child { margin-right: 0; }
  .header-rule { position: absolute; left: 0; top: 124px; width: 1200px; height: 7px; background: linear-gradient(#c9c9c9, #e6e6e6); }

  .hero { position: absolute; left: 0; top: 131px; width: 1200px; height: 422px; overflow: hidden; }
  .hero-backdrop { position: absolute; inset: 0; background: linear-gradient(90deg, var(--hero-light) 0%, #cbc3b3 30%, var(--hero-mid) 55%, #6e6b58 78%, var(--hero-dark) 100%); }
  .hero-title { position: absolute; left: 110px; top: 18px; font-family: "Roboto Condensed", Arial, sans-serif; font-weight: 700; font-size: 33px; color: var(--ink); letter-spacing: 0.3px; }
  .hero-lead { position: absolute; left: 112px; top: 70px; font-weight: 300; font-size: 25px; line-height: 28px; color: #1e1e1e; }
  .hero-copy { position: absolute; left: 112px; top: 145px; font-weight: 400; font-size: 18px; line-height: 27px; color: #1e1e1e; }
  .hero-cta-frame { position: absolute; left: 103px; top: 228px; width: 190px; height: 62px; background: rgba(150, 140, 125, 0.45); }
  .button { position: absolute; display: flex; align-items: center; justify-content: center; background: var(--button-blue); color: var(--white); font-weight: 700; font-size: 17px; text-decoration: none; }
  .hero-cta { left: 115px; top: 241px; width: 166px; height: 36px; }

  .feature { position: absolute; left: 485px; width: 191px; padding: 9px 12px 0 18px; background: var(--panel-white); border: 1px solid rgba(255,255,255,0.6); }
  .feature-title { font-size: 17px; line-height: 20px; font-weight: 400; color: var(--ink); margin-bottom: 3px; }
  .feature-body { font-size: 12px; line-height: 17.5px; color: #222; }
  .feature-core { top: 18px; height: 135px; }
  .feature-great { top: 172px; height: 101px; }
  .feature-intense { top: 293px; height: 100px; }

  .hero-product { position: absolute; left: 727px; top: 26px; width: 366px; height: 362px; background: linear-gradient(160deg, #2a2a2a 0%, #1a1a1a 55%, rgba(30,30,30,0.6) 100%); border-radius: 6px; opacity: 0.9; }
  .hero-connectors { position: absolute; left: 0; top: 0; }

  .promo-strip { position: absolute; left: 103px; top: 541px; width: 1014px; height: 287px; background: var(--white); border: 1px solid var(--rule-grey); border-top: 4px solid var(--brand-blue); display: flex; }
  .promo { position: relative; height: 100%; border-right: 1px solid var(--rule-grey); overflow: hidden; }
  .promo:last-child { border-right: none; }
  .promo-origin { width: 338px; }
  .promo-attach { width: 337px; }
  .promo-custom { flex: 1; }
  .promo-heading { position: absolute; left: 27px; top: 33px; font-weight: 300; font-size: 27px; line-height: 33px; color: var(--text-grey); z-index: 1; }
  .promo-heading .accent { color: var(--brand-blue); font-weight: 400; }
  .promo-heading .strong { color: var(--ink); font-weight: 600; font-size: 26px; }
  .promo-body { position: absolute; left: 31px; font-weight: 300; font-size: 20px; line-height: 27px; color: var(--light-grey); z-index: 1; }
  .promo-origin .promo-body { top: 147px; }
  .promo-attach .promo-heading { left: 30px; top: 33px; line-height: 32px; }
  .promo-attach .promo-heading .accent { font-weight: 300; font-size: 28px; }
  .promo-attach .promo-body { left: 30px; top: 147px; }
  .promo-custom .promo-heading { left: 30px; top: 38px; font-size: 31px; line-height: 40px; }
  .promo-custom .promo-heading .lead { color: var(--ink); font-weight: 400; }
  .promo-custom .promo-heading .accent { font-weight: 300; }
  .promo-rule { position: absolute; left: 30px; top: 167px; width: 212px; height: 1px; background: var(--rule-grey); }
  .promo-note { position: absolute; left: 31px; top: 179px; font-weight: 300; font-size: 17px; color: var(--light-grey); }
  .promo .button { top: 230px; width: 167px; height: 36px; z-index: 1; }
  .promo-origin .button { left: 21px; }
  .promo-attach .button { left: 34px; }
  .promo-custom .button { left: 27px; }
  .promo-image { position: absolute; }
  .promo-origin .promo-image { left: 225px; top: 205px; width: 110px; height: 78px; background: linear-gradient(135deg, #ffffff 20%, #cfcfcf 55%, #2a2a2a 100%); }
  .promo-attach .promo-image { left: 222px; top: 18px; width: 112px; height: 120px; background: linear-gradient(200deg, #ffffff 10%, #d0d0d0 50%, #2b2b2b 100%); }
  .promo-custom .promo-image { left: 175px; top: 26px; width: 155px; height: 82px; background: linear-gradient(120deg, #dbe9f6 0%, #9cc3e6 55%, #2d3f6b 100%); border-radius: 8px; }

  .page-fade { position: absolute; left: 0; top: 828px; width: 1200px; height: 52px; background: linear-gradient(var(--white), #f4f9fc); }
  .site-footer { position: absolute; left: 0; top: 880px; width: 1200px; height: 199px;
    background: linear-gradient(#eef6fa 0 33px, #ddeef6 33px 66px, #cfe6f2 66px 99px, #c0deee 99px 132px, #b1d6ea 132px 165px, #a7d0e6 165px 199px); }
  .footer-notice { position: absolute; left: 396px; top: 68px; font-family: "Raleway", Arial, sans-serif; font-weight: 300; font-size: 30px; line-height: 38px; color: #1e1e1e; letter-spacing: 1.5px; text-transform: uppercase; }
</style>
</head>
<body>
  <header class="site-header">
    <div class="brand">
      <span class="brand-mark"></span>
      <div class="brand-text">
        <span class="brand-name">Bramble and Pike</span>
        <span class="brand-tagline">The Equipment Security Specialists</span>
      </div>
    </div>
    <nav class="main-nav">
      <a href="#">Coiled Lanyards</a>
      <a href="#">Custom Lanyards</a>
      <a href="#">Applications</a>
      <a href="#">About Us</a>
      <a href="#">Suppliers</a>
    </nav>
  </header>
  <div class="header-rule"></div>

  <section class="hero">
    <div class="hero-backdrop" role="img" aria-label="Blurred photograph of a soldier in camouflage aiming a rifle"></div>
    <h1 class="hero-title">SECURE ANY FIREARM</h1>
    <p class="hero-lead">One product suitable<br>for multiple applications</p>
    <p class="hero-copy">State of the art technology which<br>works flawlessly everytime in action.</p>
    <div class="hero-cta-frame"></div>
    <a class="button hero-cta" href="#">Learn More</a>

    <div class="hero-product" role="img" aria-label="Photograph of a black handgun attached to a coiled lanyard"></div>

    <svg class="hero-connectors" width="1200" height="422" viewBox="0 0 1200 422" aria-hidden="true">
      <g fill="none" stroke="var(--connector)" stroke-width="1.5">
        <polyline points="676,52 713,52 713,162 920,162 920,240 1080,240"/>
        <line x1="676" y1="193" x2="795" y2="193"/>
        <line x1="676" y1="361" x2="820" y2="361"/>
      </g>
      <g fill="#7a7a7a" stroke="#e0e0e0" stroke-width="3">
        <circle cx="795" cy="193" r="7"/>
        <circle cx="1080" cy="240" r="7"/>
        <circle cx="820" cy="361" r="7"/>
      </g>
    </svg>

    <div class="feature feature-core">
      <h3 class="feature-title">Core FEATURE 1</h3>
      <p class="feature-body">The new website is to take existing text content, but all images are to be re-produced as we don't like the current version</p>
    </div>
    <div class="feature feature-great">
      <h3 class="feature-title">Great FEATURE 2</h3>
      <p class="feature-body">The new website is to take existing text content, but all images</p>
    </div>
    <div class="feature feature-intense">
      <h3 class="feature-title">Intense FEATURE 3</h3>
      <p class="feature-body">The new website is to take existing text content, but all images</p>
    </div>
  </section>

  <section class="promo-strip">
    <article class="promo promo-origin">
      <div class="promo-image" role="img" aria-label="Photograph of a black coiled lanyard with clip"></div>
      <h2 class="promo-heading">Designer of the Original<br><span class="accent">FIELD APPROVED</span><br><span class="strong">Korvex Lanyard</span></h2>
      <p class="promo-body">Works with any device,<br>equipement or firearm</p>
      <a class="button" href="#">Learn More</a>
    </article>
    <article class="promo promo-attach">
      <div class="promo-image" role="img" aria-label="Photograph of a lanyard loop with locking clip"></div>
      <h2 class="promo-heading"><span class="accent">Bramble and<br>Pike</span><br><span class="strong">your item</span></h2>
      <p class="promo-body">Works with any device,<br>equipement or firearm</p>
      <a class="button" href="#">Learn More</a>
    </article>
    <article class="promo promo-custom">
      <div class="promo-image" role="img" aria-label="Illustration of custom lanyard options around a coiled cord"></div>
      <h2 class="promo-heading"><span class="lead">We build</span><br><span class="accent">CUSTOM</span><br>lanyard solutions</h2>
      <div class="promo-rule"></div>
      <p class="promo-note">See our solutions which cater you.</p>
      <a class="button" href="#">Learn More</a>
    </article>
  </section>

  <div class="page-fade"></div>
  <footer class="site-footer">
    <p class="footer-notice">Website underconstruction<br>by Larkmoor Studio</p>
  </footer>
</body>
</html>
```